KT7 (acronym stands for Kitchentrade 7)

We are a sales and marketing start up. We sell bar and beverage dispensing equipment presently and we will add foodservice equipment to our portfolio in the coming year. We like our logo but we will consider different presentations of "KT7"

Industry/Entity Type

Marketing

```html
<!DOCTYPE html>
<html lang="en">
<head>
<meta charset="utf-8">
<title>Kitchentrade 7 – Business Card</title>
<link rel="stylesheet" href="https://fonts.googleapis.com/css2?family=Open+Sans:wght@400;600;700&display=swap">
<style>
  :root {
    --page: #e9e6e1;
    --card-black: #151515;
    --card-black-hi: #2a2a2a;
    --accent-orange: #ee7a3c;
    --orange-light: #f39a62;
    --orange-dark: #dc5f22;
    --accent-green: #7cc22a;
    --text-light: #f4f4f4;
    --deco-grey: #262626;
  }
  html, body {
    margin: 0;
    width: 1200px;
    height: 1023px;
    overflow: hidden;
    background: var(--page);
    font-family: "Open Sans", Arial, sans-serif;
  }
  .business-card {
    position: absolute;
    left: 75px;
    top: 211px;
    width: 1050px;
    height: 600px;
    border-radius: 14px;
    overflow: hidden;
    background: linear-gradient(160deg, var(--card-black-hi) 0%, var(--card-black) 55%, #0c0c0c 100%);
    box-shadow: 0 18px 40px rgba(0,0,0,.25);
  }
  .deco-band {
    position: absolute;
    right: 0;
    top: 0;
    width: 190px;
    height: 600px;
    background: linear-gradient(180deg, var(--deco-grey), #1b1b1b);
  }
  .brand {
    position: absolute;
    left: 60px;
    top: 52px;
    display: flex;
    align-items: center;
    gap: 26px;
  }
  .brand-square {
    width: 58px;
    height: 58px;
    background: var(--accent-green);
  }
  .brand-name {
    font-size: 70px;
    font-weight: 400;
    letter-spacing: 1px;
    color: var(--accent-orange);
    line-height: 1;
  }
  .holder {
    position: absolute;
    left: 60px;
    top: 172px;
    display: flex;
    align-items: baseline;
    gap: 16px;
  }
  .holder-name {
    font-size: 34px;
    font-weight: 700;
    color: var(--accent-green);
    letter-spacing: .5px;
  }
  .holder-title {
    font-size: 17px;
    font-weight: 600;
    color: var(--text-light);
    letter-spacing: 1px;
  }
  .contact-panel {
    position: absolute;
    left: 300px;
    top: 240px;
    width: 560px;
    height: 360px;
    background: linear-gradient(100deg, var(--orange-light) 0%, var(--accent-orange) 50%, var(--orange-dark) 100%);
  }
  .contact-list {
    list-style: none;
    margin: 0;
    padding: 44px 0 0 36px;
    color: var(--text-light);
    font-size: 23px;
  }
  .contact-list li {
    display: flex;
    align-items: center;
    gap: 14px;
    height: 42px;
  }
  .contact-list .gap { height: 26px; }
  .contact-list .company { font-weight: 600; }
  .icon {
    width: 22px;
    height: 22px;
    flex: none;
  }
</style>
</head>
<body>
  <div class="business-card">
    <div class="deco-band"></div>

    <div class="brand">
      <div class="brand-square"></div>
      <div class="brand-name">KITCHENTRADE 7</div>
    </div>

    <div class="holder">
      <span class="holder-name">DANA MARSH</span>
      <span class="holder-title">PRESIDENT</span>
    </div>

    <div class="contact-panel">
      <ul class="contact-list">
        <li>
          <svg class="icon" viewBox="0 0 22 22"><rect width="22" height="22" rx="3" fill="#222"/><path d="M7 5l2 0 1 3-1.5 1a7 7 0 0 0 3.5 3.5l1-1.5 3 1v2a2 2 0 0 1-2 2A10 10 0 0 1 5 7a2 2 0 0 1 2-2z" fill="#fff"/></svg>
          555.284.0196
        </li>
        <li>
          <svg class="icon" viewBox="0 0 22 22"><rect width="22" height="22" rx="3" fill="#222"/><rect x="4" y="6" width="14" height="10" fill="none" stroke="#fff" stroke-width="1.6"/><path d="M4 6l7 6 7-6" fill="none" stroke="#fff" stroke-width="1.6"/></svg>
          dana@kitchentrade7.com
        </li>
        <li>
          <svg class="icon" viewBox="0 0 22 22"><rect width="22" height="22" rx="3" fill="#222"/><circle cx="11" cy="11" r="6.5" fill="none" stroke="#fff" stroke-width="1.5"/><path d="M4.5 11h13M11 4.5c-3 3.5-3 9.5 0 13M11 4.5c3 3.5 3 9.5 0 13" fill="none" stroke="#fff" stroke-width="1.2"/></svg>
          www.kitchentrade7.com
        </li>
        <li class="gap"></li>
        <li class="company">Kitchentrade 7</li>
        <li>2400 Maple Lane, Midtown, Any City</li>
      </ul>
    </div>
  </div>
</body>
</html>
```